Business Card for Web Design consulting firm

Business card designs for Web Design consulting firm

Target Market(s)

English speaking adults ages 30 - 60. Predominantly professional services eg. Doctor, Dentist

Industry/Entity Type

Consulting

Requirements
Must have
• Double sided card

```html
<!DOCTYPE html>
<html lang="en">
<head>
<meta charset="utf-8">
<title>Pixelvane Business Card – Front and Back</title>
<link rel="stylesheet" href="https://fonts.googleapis.com/css2?family=Arimo:wght@400;700&family=Tinos&display=swap">
<style>
  :root {
    --backdrop: #9c9c9c;
    --card: #ffffff;
    --panel: #ececec;
    --panel-soft: rgba(236, 236, 236, 0.9);
    --name-blue: #1d4c8f;
    --role-blue: #3d6fae;
    --brand-grey: #6b6b6b;
    --brand-accent: #f0962a;
    --body-grey: #555555;
    --photo-light: #efe6da;
    --photo-mid: #c9b7a3;
    --photo-dark: #6f6a70;
    --shadow: rgba(30, 30, 30, 0.75);
  }
  * { box-sizing: border-box; margin: 0; padding: 0; }
  html, body {
    width: 1200px;
    height: 832px;
    overflow: hidden;
    background: var(--backdrop);
  }
  .stage { position: relative; width: 1200px; height: 832px; }

  .card {
    position: absolute;
    background: var(--card);
    box-shadow: 14px 14px 14px var(--shadow);
  }

  /* Front side */
  .card--front { left: 30px; top: 40px; width: 693px; height: 400px; z-index: 2; }
  .front__photo {
    position: absolute; left: 18px; top: 15px; width: 350px; height: 369px;
    background: linear-gradient(120deg, var(--photo-dark) 0%, var(--photo-mid) 35%, var(--photo-light) 70%, var(--photo-mid) 100%);
  }
  .front__panel {
    position: absolute; left: 378px; top: 20px; width: 300px; height: 364px;
    background: var(--panel-soft);
  }
  .front__name {
    position: absolute; right: 24px; top: 30px;
    font: 700 36px/1 "Arimo", sans-serif; color: var(--name-blue);
  }
  .front__role {
    position: absolute; right: 24px; top: 76px;
    font: 400 28px/1 "Arimo", sans-serif; color: var(--role-blue); letter-spacing: 1px;
  }
  .brand {
    position: absolute; display: flex; align-items: center; gap: 12px;
    font: 700 32px/1 "Arimo", sans-serif; color: var(--brand-grey); letter-spacing: 2px;
    white-space: nowrap;
  }
  .brand__mark { width: 22px; height: 22px; background: var(--brand-accent); flex: none; }
  .front__brand { left: 412px; top: 174px; }
  .front__address {
    position: absolute; right: 18px; top: 256px; text-align: right; font-style: normal;
    font: 400 29px/40px "Tinos", serif; color: var(--body-grey);
  }

  /* Back side */
  .card--back { left: 426px; top: 356px; width: 696px; height: 396px; z-index: 1; }
  .back__panel {
    position: absolute; left: 24px; top: 36px; width: 654px; height: 316px;
    background: var(--panel);
  }
  .back__logo-area {
    position: absolute; left: 0; top: 0; width: 306px; height: 316px;
    background: #f4f4f4;
  }
  .back__brand { left: 28px; top: 142px; }
  .back__heading {
    position: absolute; left: 324px; top: 66px;
    font: 400 28px/1 "Tinos", serif; color: var(--body-grey); letter-spacing: 1px;
  }
  .back__contacts {
    position: absolute; right: 18px; top: 153px; text-align: right; list-style: none;
    font: 400 24px/34px "Tinos", serif; color: var(--body-grey);
  }
</style>
</head>
<body>
<main class="stage">
  <section class="card card--front" aria-label="Business card front">
    <div class="front__photo" role="img" aria-label="Photo of a consultant meeting a client across a desk in a bright office"></div>
    <div class="front__panel"></div>
    <h1 class="front__name">Daniel Carter</h1>
    <p class="front__role">Sales Person</p>
    <div class="brand front__brand"><span class="brand__mark"></span>PIXELVANE</div>
    <address class="front__address">
      27 Harbour Lane,<br>Brisbane, 4000<br>Australia.
    </address>
  </section>

  <section class="card card--back" aria-label="Business card back">
    <div class="back__panel">
      <div class="back__logo-area">
        <div class="brand back__brand"><span class="brand__mark"></span>PIXELVANE</div>
      </div>
      <h2 class="back__heading">CONTACT US</h2>
      <ul class="back__contacts">
        <li>Phone: 07 5550 1234</li>
        <li>Mobile: 0400 555 321</li>
        <li>Email: hello@pixelvane.com</li>
        <li>Website www.pixelvane.com</li>
      </ul>
    </div>
  </section>
</main>
</body>
</html>
```